College Apartment Leasing Flyer

We need a post card/flyer design for a college apartment rental company called RV Stewardship Partners. We lease apartments to college students and would like a post card/flyer that appeal to college students, that are bright colors and eye catching. We would like pictures showcasing our properties with various amenities including big kitchens, living rooms with 50 inch flat screen TVs, large outdoor patios, large rooftop decks, private bathrooms, and much more. Granite countertops, hardwood floors, ceiling fans are some of the many amenities these apartments offer college students.

We want a flyer that advertises these apartments based on the pictures attached, and advertising that we are beginning to kick off our new leasing season. These apartments are ready to be rented, and we are looking to advertise these apartments to Harrowfield College college students looking for apartments.
Updates

Project Deadline Extended
Reason: I would like to see fun design elements incorporated into the flyer. Big, bold print and pictures are the main attraction

Target Market(s)

College students

Industry/Entity Type

Real Estate

Font styles to use
Sans Serif

Colors
abd037
6b449b

Requirements
Must have
• Bright colors, big bold print, pictures of college apartments
Nice to have
• I would like to see multiple pictures with BIG print
Should not have
• Animated pictures

```html
<!DOCTYPE html>
<html lang="en">
<head>
<meta charset="utf-8">
<title>RV Stewardship Partners – Leasing Flyer</title>
<link href="https://fonts.googleapis.com/css2?family=Open+Sans:wght@400;600;700;800&display=swap" rel="stylesheet">
<style>
  :root{
    --green:#abd037;
    --purple:#6b449b;
    --orange:#e8782f;
    --red:#d8262e;
    --ink:#4a4a4a;
    --white:#ffffff;
  }
  *{box-sizing:border-box;margin:0;padding:0}
  html,body{width:778px;height:1200px;overflow:hidden;background:#fff}
  body{font-family:"Open Sans",Arial,sans-serif;color:var(--ink)}
  .flyer{position:relative;width:778px;height:1200px;background:#fff;overflow:hidden}
  .abs{position:absolute}

  .figures-left{left:20px;top:22px;width:200px;height:150px;background:linear-gradient(90deg,#b9d84f,#9fc62a);border-radius:50px 50px 12px 12px;opacity:.85}
  .figures-right{right:20px;top:22px;width:150px;height:150px;background:linear-gradient(90deg,#ee8b3e,#e06d22);border-radius:50px 50px 12px 12px;opacity:.85}

  .brand{left:240px;top:30px;width:298px;text-align:center}
  .brand-mark{display:inline-block;width:64px;height:64px;border:3px solid #9a9a9a;border-radius:50%}
  .brand-name{margin-top:22px;font-size:19px;color:#555;font-weight:400;white-space:nowrap}

  .info-row{top:186px;left:0;width:778px;height:78px;display:flex;gap:6px}
  .info-address{background:var(--green);width:362px;color:var(--purple);font-weight:700;font-size:26px;line-height:1.12;padding:10px 0 0 46px}
  .info-price{background:var(--purple);width:135px;color:#fff;text-align:center;font-weight:800;font-size:31px;line-height:1;padding-top:12px}
  .info-price small{display:block;font-size:18px;font-weight:400;margin-top:2px}
  .info-stat{background:var(--orange);color:#fff;text-align:center;font-weight:800;font-size:25px;line-height:1;padding-top:16px}
  .info-stat small{display:block;font-size:10px;font-weight:600;letter-spacing:.5px;margin-top:6px}
  .stat-baths{width:75px}.stat-beds{width:75px}.stat-rent{flex:1}

  .headline{top:280px;left:0;width:778px;text-align:center;color:var(--purple);font-size:27px;font-weight:700;white-space:nowrap}
  .details{top:325px;left:0;width:778px;height:150px;background:var(--purple);color:#fff;text-align:center;font-size:16.5px;line-height:1.45;padding:14px 28px 0}

  .photo-exterior{left:0;top:490px;width:385px;height:264px;background:linear-gradient(170deg,#c9ccc9,#8c8275 60%,#6e6a60)}
  .photo-skyline{left:393px;top:490px;width:385px;height:264px;background:linear-gradient(180deg,#6fa0d8,#a9c6e6 55%,#6e7b68)}
  .photo-kitchen{left:0;top:762px;width:250px;height:204px;background:linear-gradient(150deg,#e9e6e2,#8a2a26 60%,#3b2b22)}
  .photo-living{left:258px;top:762px;width:262px;height:204px;background:linear-gradient(150deg,#e8e4de,#7a5233 70%,#3a2a1e)}
  .photo-bedroom{left:528px;top:762px;width:250px;height:204px;background:linear-gradient(150deg,#f1efec,#c9c2b8 60%,#8a7a66)}

  .cta{top:982px;left:0;width:778px;text-align:center;color:var(--orange);font-weight:800;font-size:20px;white-space:nowrap}
  .phone{top:1010px;left:0;width:778px;text-align:center;color:var(--red);font-weight:800;font-size:60px;line-height:1.3;white-space:nowrap}

  .footer{left:0;top:1112px;width:778px;height:88px;display:flex}
  .footer-site{flex:1;background:var(--green);color:#fff;font-weight:700;font-size:34px;display:flex;align-items:center;padding-left:46px}
  .footer-accent{width:118px;background:var(--purple)}
</style>
</head>
<body>
<main class="flyer">
  <div class="abs figures-left" role="img" aria-label="Green silhouettes of cheering students"></div>
  <div class="abs figures-right" role="img" aria-label="Orange silhouettes of cheering students"></div>

  <header class="abs brand">
    <span class="brand-mark"></span>
    <p class="brand-name">RV Stewardship Partners, Llc</p>
  </header>

  <section class="abs info-row">
    <div class="info-address">1426 Alder St<br>Lower Unit</div>
    <div class="info-price">$640<small>per BDRM</small></div>
    <div class="info-stat stat-baths">3.5<small>BATHS</small></div>
    <div class="info-stat stat-beds">4<small>BEDS</small></div>
    <div class="info-stat stat-rent">$2,560<small>RENT</small></div>
  </section>

  <h1 class="abs headline">NEW Construction blocks from Harrowfield College!</h1>

  <p class="abs details">Beautiful 4BR/3.5BA unit on Alder St. with upgraded amenities including: GRANITE COUNTER TOPS, NEW APPLIANCES, SPACIOUS BEDROOMS AND CLOSETS, HARDWOOD FLOORS, SECURITY SYSTEM, OUTDOOR PATIO, SECURITY CAMERAS, SURROUND SOUND IN LIVING ROOM AND PATIO, CEILING FANS, WASHER AND DRYER, AND MORE!</p>

  <div class="abs photo-exterior" role="img" aria-label="Rear exterior of the building with wooden steps and patio"></div>
  <div class="abs photo-skyline" role="img" aria-label="City skyline view from the rooftop deck"></div>
  <div class="abs photo-kitchen" role="img" aria-label="Kitchen with red cabinets and granite counters"></div>
  <div class="abs photo-living" role="img" aria-label="Living room with hardwood floors and flat screen TV"></div>
  <div class="abs photo-bedroom" role="img" aria-label="Bright bedroom with closet"></div>

  <p class="abs cta">WE HAVE MANY UNITS TO CHOOSE FROM, CONTACT US TODAY!</p>
  <p class="abs phone">T: 215-555-0148</p>

  <footer class="abs footer">
    <div class="footer-site">rvstewardship.com</div>
    <div class="footer-accent"></div>
  </footer>
</main>
</body>
</html>
```